Birchford Realty Business Card

Business Card:

Somewhere on front of card, please include Broker License Number: 5839162

Website is BirchfordRealty.example

Address is:
7218 Crestover Ave E
Saginaw, MI 48271

I'll let you use creative freedom on the rest; we obviously need Name, Title, Email (@BirchfordRealty.example), Office Phone, Cell Phone.

Don't want any special die-cutting, just a standard size business card.

On the back, include a place for the date and time of an appointment to be written in pen.

Requirements
Must have
• Our logo, attached to email.

```html
<!DOCTYPE html>
<html lang="en">
<head>
<meta charset="utf-8">
<title>Birchford Realty Business Card</title>
<link rel="stylesheet" href="https://fonts.googleapis.com/css2?family=Open+Sans:wght@700&family=Arimo:wght@400;700&display=swap">
<style>
  :root {
    --stage: #e9e7e3;
    --navy: #34337a;
    --ink: #1a1a1a;
    --paper: #f4f3f0;
    --white: #ffffff;
    --grey: #8c8c94;
  }
  * { margin: 0; padding: 0; box-sizing: border-box; }
  html, body { width: 1200px; height: 892px; overflow: hidden; background: var(--stage); }
  .canvas { position: relative; width: 1200px; height: 892px; }
  .card {
    position: absolute; left: 250px; width: 700px; height: 400px;
    overflow: hidden; box-shadow: 0 4px 14px rgba(0,0,0,.18);
    font-family: "Arimo", Arial, sans-serif;
  }
  .card--front { top: 466px; background: var(--paper); }
  .card--back { top: 26px; background: var(--white); }
  .card__art { position: absolute; inset: 0; width: 700px; height: 400px; }

  .wordmark {
    position: absolute; font-family: "Open Sans", sans-serif; font-weight: 700;
    letter-spacing: .5px; white-space: nowrap;
  }
  .card--front .wordmark { left: 220px; top: 62px; font-size: 46px; color: var(--navy); }
  .license { position: absolute; left: 226px; top: 128px; font-size: 18px; color: var(--grey); font-weight: 700; }

  .person { position: absolute; left: 34px; top: 262px; color: var(--white); }
  .person__name { font-size: 28px; font-weight: 700; white-space: nowrap; }
  .person__title { font-size: 18px; margin-top: 2px; }

  .divider { position: absolute; left: 262px; top: 284px; width: 2px; height: 108px; background: var(--white); }
  .contact { position: absolute; left: 276px; top: 286px; list-style: none; color: var(--white); font-size: 16px; }
  .contact li { display: flex; align-items: center; height: 21px; white-space: nowrap; }
  .contact svg { width: 14px; height: 14px; margin-right: 11px; flex: none; }

  .card--back .wordmark { right: 40px; top: 48px; font-size: 50px; color: var(--white); }
  .appointment { position: absolute; left: 40px; top: 186px; right: 40px; color: var(--ink); }
  .appointment__heading { font-size: 32px; font-weight: 400; margin-bottom: 18px; }
  .appointment__field { display: flex; align-items: flex-end; font-size: 28px; height: 48px; }
  .appointment__line { flex: 1; margin-left: 10px; margin-bottom: 6px; border-bottom: 3px dotted var(--ink); }
</style>
</head>
<body>
<main class="canvas">

  <section class="card card--back">
    <svg class="card__art" viewBox="0 0 700 400" aria-hidden="true">
      <defs>
        <linearGradient id="band" x1="0" y1="0" x2="1" y2="1">
          <stop offset="0" stop-color="#2c2b7e"/>
          <stop offset="1" stop-color="#4f4e9e"/>
        </linearGradient>
      </defs>
      <rect x="0" y="0" width="700" height="150" fill="url(#band)"/>
      <rect x="0" y="150" width="700" height="6" fill="var(--white)"/>
      <rect x="0" y="156" width="700" height="5" fill="var(--navy)"/>
    </svg>
    <div class="wordmark">Birchford Realty</div>
    <div class="appointment">
      <h2 class="appointment__heading">Appoinments</h2>
      <div class="appointment__field">Date :<span class="appointment__line"></span></div>
      <div class="appointment__field">Time :<span class="appointment__line"></span></div>
    </div>
  </section>

  <section class="card card--front">
    <svg class="card__art" viewBox="0 0 700 400" aria-hidden="true">
      <path d="M0,100 C120,275 420,300 700,268 L700,400 L0,400 Z" fill="var(--ink)"/>
      <path d="M40,112 C170,265 430,280 660,262" fill="none" stroke="var(--navy)" stroke-width="4"/>
    </svg>
    <div class="wordmark">Birchford Realty</div>
    <div class="license">Lic No: 5839162</div>

    <div class="person">
      <div class="person__name">Dana Whitfield</div>
      <div class="person__title">CEO</div>
    </div>
    <div class="divider"></div>
    <ul class="contact">
      <li><svg viewBox="0 0 16 16"><rect x="1" y="5" width="14" height="9" rx="2" fill="#fff"/><path d="M3 5 Q8 0 13 5" fill="none" stroke="#fff" stroke-width="2"/></svg>021-5550-3816</li>
      <li><svg viewBox="0 0 16 16"><rect x="4" y="1" width="8" height="14" rx="1.5" fill="#fff"/><rect x="5.5" y="3" width="5" height="8" fill="#1a1a1a"/></svg>022-5550-7243</li>
      <li><svg viewBox="0 0 16 16"><rect x="1" y="3" width="14" height="10" fill="#fff"/><path d="M1 3 L8 9 L15 3" fill="none" stroke="#1a1a1a" stroke-width="1.5"/></svg>dana@BirchfordRealty.example</li>
      <li><svg viewBox="0 0 16 16"><circle cx="8" cy="8" r="7" fill="none" stroke="#fff" stroke-width="1.6"/><ellipse cx="8" cy="8" rx="3" ry="7" fill="none" stroke="#fff" stroke-width="1.2"/><path d="M1 8 H15" stroke="#fff" stroke-width="1.2"/></svg>www.BirchfordRealty.example</li>
      <li><svg viewBox="0 0 16 16"><path d="M8 15 C3 9 3 6 3 6 A5 5 0 0 1 13 6 C13 6 13 9 8 15 Z" fill="#fff"/><circle cx="8" cy="6" r="2" fill="#1a1a1a"/></svg>7218 Crestover Ave E, Saginaw, MI 48271</li>
    </ul>
  </section>

</main>
</body>
</html>
```